Online Certificate in Research Methods needs a Digital Banner ad

We are launching an online graduate certificate in Quantitative and Qualitative Social Science Research Methods. We need a digital banner created so we can advertise on pagenook, seekora, and some other places.

The banner needs to use these color schemes and fonts: https://universityrelations.bmlu.edu/brand-guide/color

Would like the banner to say (either as three lines, or if not in three lines, have these sets of words at minimum on the same line):
Online Graduate Certificate in
Quantitative & Qualitative
Social Science Research Methods

We also want it to say Brennmoor Lake University and Next Start Date August 18, 2021. I’ve attached a picture of a version we tried to create but is hard to read.

We need a graphic that looks good in the following specs:
600px wide x 70px tall, high quality (at least 300 dpi) jpg or png

And
Pagenook recommendations:
Design Recommendations
• File Type: JPG or PNG
• Ratio: 1.91:1 to 1:1
• Resolution: At least 1080 x 1080 pixels
Text Recommendations
• Primary Text: 125 characters
• Headline: 40 characters
• Description: 30 characters
Technical Requirements
• Maximum File Size: 30MB
• Minimum Width: 600 pixels
• Minimum Height: 600 pixels
• Aspect Ratio Tolerance: 3%

```html
<!DOCTYPE html>
<html lang="en">
<head>
<meta charset="utf-8">
<title>Brennmoor Lake University – Online Graduate Certificate Banners</title>
<link rel="stylesheet" href="https://fonts.googleapis.com/css2?family=Lexend:wght@300;400;600;700&display=swap">
<style>
  :root {
    --navy: #002855;
    --gold: #eaaa00;
    --white: #ffffff;
    --page: #ffffff;
    --photo-a: #8a6a4c;
    --photo-b: #3f7d72;
    --photo-c: #d9a48c;
  }
  * { box-sizing: border-box; margin: 0; padding: 0; }
  html, body {
    width: 1200px; height: 1200px; overflow: hidden;
    background: var(--page);
    font-family: "Lexend", "Helvetica Neue", Arial, sans-serif;
  }
  .canvas { position: relative; width: 1200px; height: 1200px; }

  .banner { position: absolute; background: var(--navy); overflow: hidden; color: var(--white); }
  .banner--landscape { left: 189px; top: 14px; width: 734px; height: 385px; }
  .banner--square { left: 262px; top: 426px; width: 590px; height: 587px; }
  .banner--leaderboard { left: 5px; top: 1036px; width: 1190px; height: 140px; }

  .photo {
    position: absolute; top: 0; right: 0; height: 100%;
    background: linear-gradient(135deg, var(--photo-a) 0%, var(--photo-c) 45%, var(--photo-b) 100%);
  }
  .shapes { position: absolute; inset: 0; width: 100%; height: 100%; }
  .shape--gold { fill: var(--gold); }
  .shape--white { fill: var(--white); }

  .accent-bar { position: absolute; width: 5px; background: var(--gold); }

  .wordmark {
    position: absolute; display: flex; align-items: center; gap: 8px;
    font-weight: 400; color: var(--white); white-space: nowrap; letter-spacing: -0.01em;
  }
  .wordmark__square { width: 0.8em; height: 0.8em; background: var(--gold); flex: none; }

  .headline { position: absolute; font-weight: 600; line-height: 1.35; white-space: nowrap; }
  .program { position: absolute; font-weight: 300; line-height: 1.3; white-space: nowrap; }

  .start-date, .cta {
    position: absolute; font-weight: 600; color: var(--navy); white-space: nowrap;
    display: flex; align-items: center;
  }
  .cta { font-weight: 700; letter-spacing: 0.02em; justify-content: center; }

  /* Landscape */
  .banner--landscape .photo { width: 280px; clip-path: polygon(128px 0, 280px 0, 280px 385px, 152px 385px, 2px 189px); }
  .banner--landscape .accent-bar { left: 11px; top: 77px; height: 254px; }
  .banner--landscape .wordmark { left: 27px; top: 25px; font-size: 22px; }
  .banner--landscape .headline { left: 30px; top: 108px; font-size: 27px; }
  .banner--landscape .program { left: 30px; width: 360px; top: 166px; font-size: 25px; text-align: center; }
  .banner--landscape .start-date { left: 11px; top: 323px; height: 42px; font-size: 18px; }
  .banner--landscape .cta { left: 365px; top: 323px; width: 210px; height: 42px; font-size: 17px; }

  /* Square */
  .banner--square .photo { width: 281px; clip-path: polygon(180px 47px, 281px 47px, 281px 444px, 184px 444px, 27px 242px); }
  .banner--square .accent-bar { left: 12px; top: 124px; height: 381px; }
  .banner--square .wordmark { left: 24px; top: 35px; font-size: 25px; }
  .banner--square .headline { left: 32px; top: 124px; font-size: 40px; }
  .banner--square .program { left: 35px; top: 338px; font-size: 24px; }
  .banner--square .start-date { left: 24px; top: 506px; height: 45px; font-size: 20px; }
  .banner--square .cta { left: 398px; top: 506px; width: 190px; height: 45px; font-size: 17px; }

  /* Leaderboard */
  .banner--leaderboard .photo { width: 260px; clip-path: polygon(62px 0, 260px 0, 260px 140px, 95px 140px, 30px 73px); }
  .banner--leaderboard .accent-bar { left: 30px; top: 5px; height: 130px; }
  .banner--leaderboard .wordmark { left: 474px; top: 28px; font-size: 22px; }
  .banner--leaderboard .headline { left: 53px; top: 17px; font-size: 22px; }
  .banner--leaderboard .program { left: 60px; top: 60px; font-size: 23px; line-height: 1.22; }
  .banner--leaderboard .start-date { left: 483px; top: 97px; height: 41px; font-size: 18px; }
  .banner--leaderboard .cta { left: 815px; top: 97px; width: 160px; height: 41px; font-size: 15px; }
</style>
</head>
<body>
<main class="canvas">

  <section class="banner banner--landscape" aria-label="Landscape banner">
    <div class="photo" role="img" aria-label="Photo of a smiling student holding a red folder, headphones around her neck"></div>
    <svg class="shapes" viewBox="0 0 734 385" aria-hidden="true">
      <polygon class="shape--gold" points="548,0 584,0 457,189 607,385 572,385 422,189"/>
      <polygon class="shape--white" points="0,323 343,323 368,365 0,365"/>
      <polygon class="shape--white" points="355,323 555,323 580,365 380,365"/>
    </svg>
    <div class="accent-bar"></div>
    <div class="wordmark"><span class="wordmark__square"></span>Brennmoor Lake University</div>
    <h2 class="headline">Online Graduate Certificate</h2>
    <p class="program">Quantitative &amp; Qualitative<br>Social Science Research<br>Methods</p>
    <p class="start-date">Next Start Date August 18, 2021</p>
    <p class="cta">LEARN MORE</p>
  </section>

  <section class="banner banner--square" aria-label="Square banner">
    <div class="photo" role="img" aria-label="Photo of a smiling student holding a red folder, headphones around her neck"></div>
    <svg class="shapes" viewBox="0 0 590 587" aria-hidden="true">
      <path class="shape--gold" fill-rule="evenodd" d="M462,27 H590 V464 H474 L301,242 Z M489,47 H590 V444 H493 L336,242 Z"/>
      <polygon class="shape--white" points="0,506 406,506 432,551 0,551"/>
      <polygon class="shape--white" points="386,506 590,506 590,551 414,551"/>
    </svg>
    <div class="accent-bar"></div>
    <div class="wordmark"><span class="wordmark__square"></span>Brennmoor Lake University</div>
    <h2 class="headline">Online<br>Graduate<br>Certificate</h2>
    <p class="program">Quantitative &amp; Qualitative<br>Social Science Research<br>Methods</p>
    <p class="start-date">Next Start Date August 18, 2021</p>
    <p class="cta">LEARN MORE</p>
  </section>

  <section class="banner banner--leaderboard" aria-label="Leaderboard banner">
    <div class="photo" role="img" aria-label="Photo of a smiling student holding a red folder in a wooden hallway"></div>
    <svg class="shapes" viewBox="0 0 1190 140" aria-hidden="true">
      <polygon class="shape--gold" points="962,0 992,0 960,73 1025,140 995,140 928,73"/>
      <polygon class="shape--white" points="467,97 790,97 812,138 467,138"/>
      <polygon class="shape--white" points="800,97 965,97 985,138 822,138"/>
    </svg>
    <div class="accent-bar"></div>
    <h2 class="headline">Online Graduate Certificate</h2>
    <p class="program">Quantitative &amp; Qualitative<br>Social Science Research Methods</p>
    <div class="wordmark"><span class="wordmark__square"></span>Brennmoor Lake University</div>
    <p class="start-date">Next Start Date August 18, 2021</p>
    <p class="cta">LEARN MORE</p>
  </section>

</main>
</body>
</html>
```